Wordpress Design Project (Darvy)

We need a wordpress design for an established auction and real estate company based in Pennsylvania. The winning design will incorporate a professional layout with and company logo in a very simple and clean layout.

Industry/Entity Type

Real Estate

Requirements
Must have
• Navigation:
1) Home; 2) Auctions; 3) Appraisals; 4) Real Estate; 5) FAQ; 6) About Us; 7) Contact Us.

Site will have overall layout of https://www.plumvesta.com/featured/regions/the-northeast. Home page will have logo and navigation at top. The navigation bar will also have social media icons (facebook, Google+, RSS, twitter) inside it. There will be text in the content area - use lorem ipsum. The image attached will be used below text (auctions.jpg) . Footer will have smaller company loogo, the attached affiliation logos and social media icons.

Logo attached. Color scheme will be black, gray, and red as accent color.
Nice to have
• navigation will have dropdowns, nice to have one represented - under auctions 'All Auctions' will be dropdown.

```html
<!DOCTYPE html>
<html lang="en">
<head>
<meta charset="utf-8">
<title>Darvy Auctioneers &amp; Appraisers</title>
<link href="https://fonts.googleapis.com/css2?family=Cinzel:wght@400&family=Hind:wght@400;500;600&family=Lora:wght@400&display=swap" rel="stylesheet">
<style>
:root{
  --red:#d9241f;
  --red-soft:#e2463f;
  --red-dark:#6e1512;
  --ink:#2b2b2b;
  --grey-text:#3a3a3a;
  --panel:#e3e3e3;
  --page:#f2f2f2;
  --white:#ffffff;
  --line:#c9c9c9;
  --footer-soft:#f6c9c7;
}
*{box-sizing:border-box;margin:0;padding:0}
html,body{width:1079px;height:1200px;overflow:hidden;background:var(--page);font-family:"Hind",Arial,sans-serif;color:var(--ink)}
.page{position:relative;width:1079px;height:1200px}
.site-header{position:absolute;left:0;top:0;width:1079px;height:85px;background:#f7f7f7;box-shadow:0 2px 4px rgba(0,0,0,.15)}
.brand{position:absolute;left:74px;top:22px;font-family:"Hind",sans-serif;font-weight:600;font-size:34px;line-height:1;color:var(--ink)}
.main-nav{position:absolute;top:50px;left:344px;display:flex}
.main-nav a{font-size:12.5px;color:var(--red);text-decoration:none;margin-right:52px}
.main-nav a.active{color:var(--ink);text-decoration:underline}
.dropdown{position:absolute;left:424px;top:78px;width:144px}
.dropdown a{display:block;height:23.5px;line-height:25px;padding-left:11px;font-size:11px;color:var(--white);text-decoration:none;background:var(--red-soft);border-bottom:1px solid rgba(255,255,255,.25)}
.dropdown a.current{background:var(--red-dark)}
.intro{position:absolute;left:76px;top:103px;width:928px;height:301px;background:var(--panel);border:1px solid #fff;box-shadow:0 0 0 1px #ddd;text-align:center}
.intro h1{font-family:"Cinzel",serif;font-weight:400;font-size:28px;color:var(--red);margin-top:28px;letter-spacing:1px}
.intro h2{font-family:Arial,sans-serif;font-weight:400;font-size:19.5px;color:var(--grey-text);margin-top:2px;letter-spacing:.3px}
.intro hr{border:0;border-top:1px solid var(--line);width:898px;margin:5px auto 0}
.intro p{font-size:12.6px;line-height:19.6px;color:var(--grey-text);width:880px;margin:22px auto 0}
.intro p + p{line-height:18px;margin-top:16px}
.lot{position:absolute;width:420px}
.lot-photo{display:block;width:414px;height:187px;border:2px solid #fff}
.lot-title{font-family:"Lora",serif;font-weight:400;font-size:19.5px;color:var(--ink);margin-top:10px}
.lot-loc{position:absolute;right:0;top:199px;font-size:13px;font-weight:600;color:var(--ink);display:flex;align-items:center;gap:6px}
.lot-meta{font-size:12px;line-height:18px;color:var(--grey-text);margin-top:2px}
.lot.hover .lot-title,.lot.hover .lot-meta{color:var(--red);text-decoration:underline}
.site-footer{position:absolute;left:0;top:1037px;width:1079px;height:163px;background:var(--red);border-top:8px solid #dedede}
.copyright{position:absolute;left:76px;top:20px;font-size:12px;color:var(--white);font-weight:500}
.social{position:absolute;right:72px;top:15px;display:flex;align-items:center;gap:9px;font-size:13px;color:var(--white);font-weight:500}
.social span{margin-right:3px}
.social i{width:26px;height:26px;border-radius:50%;background:var(--white);display:block}
.affiliations{position:absolute;left:427px;top:90px;display:flex;align-items:center;gap:26px}
.footer-brand{color:var(--footer-soft);font-size:28px;font-weight:500;line-height:1}
.badge{width:46px;height:46px;border-radius:50%;border:2px solid #f1a9a6;display:block}
.badge.sq{border-radius:4px;width:34px}
</style>
</head>
<body>
<div class="page">
  <header class="site-header">
    <div class="brand">Darvy</div>
    <nav class="main-nav">
      <a href="#">Home</a>
      <a href="#" class="active">Auctions</a>
      <a href="#">Appraisals</a>
      <a href="#">Real Estate</a>
      <a href="#">FAQ</a>
      <a href="#">About Us</a>
      <a href="#">Contact Us</a>
    </nav>
  </header>

  <section class="intro">
    <h1>Lorem Ipsum passages, and more recently with desktop</h1>
    <h2>when an unknown printer took a galley of type &amp; scrambled it to make a type specimen</h2>
    <hr>
    <p>There are many variations of passages of Lorem Ipsum available, but the majority have suffered alteration in some form, by injected humour, or randomised words which don't look even slightly believable. If you are going to use a passage of Lorem Ipsum, you need to be sure there isn't anything embarrassing hidden in the middle of text. All the Lorem Ipsum generators on the Internet tend to repeat predefined chunks as necessary, making this the first true generator on the Internet. It uses a dictionary of over 200 Latin words, combined with a handful of model sentence structures,</p>
    <p>Lorem Ipsum available, but the majority have suffered alteration in some form, by injected humour, or randomised words which don't look even slightly believable. If you are going to use a passage of Lorem Ipsum, you need to be sure there isn't anything embarrassing hidden in the middle of text. All the Lorem Ipsum generators on the Internet tend to repeat predefined chunks as necessary.</p>
  </section>

  <nav class="dropdown">
    <a href="#">Darvy Auctioneers #1</a>
    <a href="#" class="current">Darvy Auctioneers #2</a>
    <a href="#">Darvy Auctioneers #3</a>
  </nav>

  <div class="lots">
    <article class="lot hover" style="left:96px;top:449px">
      <div class="lot-photo" role="img" aria-label="Warehouse row of wooden cabinets with yellow lot tags" style="background:linear-gradient(90deg,#9a5a3a,#6b2d22 45%,#8a4a35)"></div>
      <span class="lot-loc"><svg width="16" height="22" viewBox="0 0 16 22"><path d="M8 0a8 8 0 0 1 8 8c0 6-8 14-8 14S0 14 0 8a8 8 0 0 1 8-8z" fill="#ccc"/><circle cx="8" cy="8" r="4" fill="#d9241f"/></svg>New York, NK</span>
      <h3 class="lot-title">Lorem Ipsum passages</h3>
      <p class="lot-meta">It was popularised in the 1960s with the release<br>13 Aug 2013</p>
    </article>
    <article class="lot" style="left:565px;top:449px">
      <div class="lot-photo" role="img" aria-label="Bathroom vanities with dark granite tops" style="border:0;width:416px;background:linear-gradient(180deg,#3a2a24 30%,#b4562a 55%,#8e3e1e)"></div>
      <span class="lot-loc"><svg width="16" height="22" viewBox="0 0 16 22"><path d="M8 0a8 8 0 0 1 8 8c0 6-8 14-8 14S0 14 0 8a8 8 0 0 1 8-8z" fill="#ccc"/><circle cx="8" cy="8" r="4" fill="#d9241f"/></svg>New York, NK</span>
      <h3 class="lot-title">Lorem Ipsum passages</h3>
      <p class="lot-meta">It was popularised in the 1960s with the release<br>13 Aug 2013</p>
    </article>
    <article class="lot" style="left:98px;top:731px">
      <div class="lot-photo" role="img" aria-label="Stacked rolls of carpet with yellow lot tags" style="border:0;background:linear-gradient(135deg,#8d8168,#9c9a92 50%,#6e6c68)"></div>
      <span class="lot-loc"><svg width="16" height="22" viewBox="0 0 16 22"><path d="M8 0a8 8 0 0 1 8 8c0 6-8 14-8 14S0 14 0 8a8 8 0 0 1 8-8z" fill="#ccc"/><circle cx="8" cy="8" r="4" fill="#d9241f"/></svg>New York, NK</span>
      <h3 class="lot-title">Lorem Ipsum passages</h3>
      <p class="lot-meta">It was popularised in the 1960s with the release<br>13 Aug 2013</p>
    </article>
    <article class="lot" style="left:564px;top:731px">
      <div class="lot-photo" role="img" aria-label="Row of white glass-paned doors in a warehouse" style="border:0;width:417px;background:linear-gradient(90deg,#c9d7ec,#e8eef7 50%,#b89a6e)"></div>
      <span class="lot-loc"><svg width="16" height="22" viewBox="0 0 16 22"><path d="M8 0a8 8 0 0 1 8 8c0 6-8 14-8 14S0 14 0 8a8 8 0 0 1 8-8z" fill="#ccc"/><circle cx="8" cy="8" r="4" fill="#d9241f"/></svg>New York, NK</span>
      <h3 class="lot-title">Lorem Ipsum passages</h3>
      <p class="lot-meta">It was popularised in the 1960s with the release<br>13 Aug 2013</p>
    </article>
  </div>

  <footer class="site-footer">
    <p class="copyright">Copyright © 2007 - 2013 - Darvy Auctioneers &amp; Appraisers . - All Rights Reserved.</p>
    <div class="social"><span>Stay Connected</span><i></i><i></i><i></i><i></i></div>
    <div class="affiliations">
      <div class="footer-brand">Darvy</div>
      <i class="badge sq"></i><i class="badge"></i><i class="badge"></i><i class="badge sq"></i><i class="badge sq"></i><i class="badge"></i>
    </div>
  </footer>
</div>
</body>
</html>
```